New Flyer Design Project

Needing brochure explaining the benefits of a home sleep study compared to a clinical hospital sleep study. We had our company logo designed by Vantro Works, we love it. We would like for it to be a bi-fold. See attachments for examples of information we would like to include.

```html
<!DOCTYPE html>
<html lang="en">
<head>
<meta charset="utf-8">
<title>Prairie Airway and Sleep Care – Home Sleep Study Brochure</title>
<link rel="stylesheet" href="https://fonts.googleapis.com/css2?family=Antonio:wght@600;700&family=Fira+Sans+Extra+Condensed:ital,wght@0,400;0,600;0,700;1,400&display=swap">
<style>
  :root {
    --green: #5b9e3c;
    --green-deep: #4f9a32;
    --lime: #cde216;
    --navy: #0b2e5e;
    --navy-text: #0c2d5e;
    --cyan: #2bb6d6;
    --sky: #1e9be0;
    --white: #ffffff;
    --band-text: #26361c;
  }
  * { margin: 0; padding: 0; box-sizing: border-box; }
  html, body { width: 1200px; height: 927px; overflow: hidden; background: var(--white); }
  body { font-family: "Fira Sans Extra Condensed", "Arial Narrow", sans-serif; }

  .brochure { position: relative; width: 1200px; height: 927px; overflow: hidden; }

  .panel-inside { position: absolute; left: 0; top: 0; width: 600px; height: 927px; background: var(--green); }
  .panel-cover { position: absolute; left: 600px; top: 0; width: 600px; height: 927px; background: var(--white); }

  .steps-title {
    position: absolute; left: 0; top: 68px; width: 600px; text-align: center;
    font-family: "Antonio", "Arial Narrow", sans-serif; font-weight: 700;
    color: var(--white); font-size: 36px; line-height: 39px; letter-spacing: 0.2px;
  }
  .intro-band {
    position: absolute; left: 0; top: 161px; width: 600px; height: 64px; background: var(--lime);
    display: flex; align-items: center; justify-content: center; text-align: center;
    color: var(--band-text); font-weight: 700; font-size: 17px; line-height: 24px;
  }
  .step { position: absolute; left: 0; width: 600px; }
  .step-icon { position: absolute; left: 138px; width: 48px; height: 48px; }
  .step-text { position: absolute; left: 239px; width: 232px; color: var(--white); font-size: 17.5px; line-height: 24px; }
  .step-text strong { font-weight: 700; }

  .motto {
    position: absolute; left: 0; top: 646px; width: 600px; text-align: center;
    font-family: "Antonio", "Arial Narrow", sans-serif; font-weight: 700; color: var(--white); font-size: 31px;
  }
  .motto-note {
    position: absolute; left: 0; top: 694px; width: 600px; text-align: center;
    color: var(--white); font-size: 20.5px; line-height: 28px;
  }

  .waves { position: absolute; left: 0; top: 0; width: 1200px; height: 927px; }

  .contact-heading { position: absolute; left: 0; top: 806px; width: 600px; text-align: center; color: var(--white); font-weight: 700; font-size: 18px; }
  .contact-address { position: absolute; left: 98px; top: 843px; color: var(--white); font-size: 17.5px; line-height: 18px; }
  .contact-phone { position: absolute; left: 355px; color: var(--white); font-size: 17.5px; }

  .brand { position: absolute; left: 650px; top: 36px; display: flex; align-items: center; gap: 10px; }
  .brand-mark { width: 22px; height: 22px; background: var(--green-deep); }
  .brand-name { font-weight: 600; font-size: 27px; color: var(--navy-text); }

  .cover-title {
    position: absolute; left: 600px; top: 120px; width: 600px; text-align: center;
    font-family: "Antonio", "Arial Narrow", sans-serif; font-weight: 700;
    font-size: 64px; line-height: 78px; letter-spacing: -1.5px;
  }
  .cover-title .line-navy { display: block; color: var(--navy-text); }
  .cover-title .line-green { display: block; color: var(--green-deep); }

  .cover-photo {
    position: absolute; left: 630px; top: 300px; width: 570px; height: 540px;
    background:
      radial-gradient(ellipse at 70% 45%, #7b93b8 0%, #a9b7cc 28%, #dfe3ea 55%, rgba(255,255,255,0) 78%),
      linear-gradient(160deg, #ffffff 0%, #eef0f3 60%, #c9a882 100%);
  }
  .cover-lede { position: absolute; left: 636px; top: 323px; width: 240px; color: var(--navy-text); }
  .cover-lede strong { display: block; font-weight: 700; font-size: 24px; line-height: 36px; }
  .cover-lede span { display: block; font-size: 25px; line-height: 36px; }

  .cover-footer { position: absolute; left: 600px; top: 839px; width: 600px; text-align: center; color: var(--white); }
  .cover-footer .footer-name { font-weight: 700; font-size: 20px; }
  .cover-footer .footer-tagline { font-style: italic; font-size: 19.5px; margin-top: 4px; }
</style>
</head>
<body>
<main class="brochure">

  <section class="panel-inside">
    <h2 class="steps-title">3 SIMPLE STEPS<br>TO RECLAIM YOUR ENERGY</h2>
    <p class="intro-band">Improving your sleep shouldn't be stressful. At Prairie Airway and<br>Sleep Care, we make the process completely seamless:</p>

    <div class="step" style="top:256px">
      <svg class="step-icon" style="top:8px" viewBox="0 0 48 48" aria-hidden="true">
        <rect x="14" y="2" width="26" height="14" rx="6" fill="#fff"/>
        <path d="M30 16 l4 6 l0 -6z" fill="#fff"/>
        <rect x="4" y="10" width="16" height="10" rx="5" fill="#fff" stroke="var(--green)" stroke-width="2"/>
        <circle cx="10" cy="30" r="5" fill="#fff"/>
        <path d="M2 46 a8 8 0 0 1 16 0z" fill="#fff"/>
        <circle cx="36" cy="30" r="6" fill="#fff"/>
        <path d="M26 46 a10 9 0 0 1 20 0z" fill="#fff"/>
      </svg>
      <p class="step-text"><strong>Consultation:</strong> Speak with our dedicated team about your sleep symptoms.</p>
    </div>

    <div class="step" style="top:352px">
      <svg class="step-icon" style="top:10px" viewBox="0 0 48 48" aria-hidden="true">
        <path d="M24 6 L44 14 L24 22 L4 14z" fill="#fff"/>
        <path d="M6 22 L24 29 L24 46 L6 38z" fill="#fff"/>
        <path d="M42 22 L24 29 L24 46 L42 38z" fill="#fff"/>
        <path d="M4 14 L24 22 L44 14" fill="none" stroke="var(--green)" stroke-width="2"/>
      </svg>
      <p class="step-text"><strong>Pick Up Your Device:</strong> Receive a quick, easy demonstration on how to wear the lightweight device.</p>
    </div>

    <div class="step" style="top:448px">
      <svg class="step-icon" style="top:36px" viewBox="0 0 48 48" aria-hidden="true">
        <rect x="4" y="10" width="36" height="22" rx="3" fill="#fff"/>
        <circle cx="20" cy="18" r="5" fill="var(--green)"/>
        <path d="M10 30 a10 8 0 0 1 20 0z" fill="var(--green)"/>
        <text x="34" y="10" font-size="10" font-weight="700" fill="#fff" font-family="sans-serif">z</text>
        <rect x="2" y="36" width="44" height="4" fill="#fff"/>
        <rect x="2" y="42" width="44" height="4" fill="#fff"/>
      </svg>
      <p class="step-text"><strong>Sleep &amp; Return:</strong> Sleep comfortably at home for one night, return the device the next day, and let our sleep specialists analyze your results to build a customized therapy plan.</p>
    </div>
  </section>

  <section class="panel-cover">
    <div class="cover-photo" role="img" aria-label="Photo of a woman sleeping comfortably in bed at home while wearing a home sleep test device, with a bedside clock and tubing"></div>
  </section>

  <svg class="waves" viewBox="0 0 1200 927" aria-hidden="true">
    <path d="M0 715 C120 755 250 785 400 790 C500 792 560 770 600 758 L600 927 L0 927z" fill="var(--cyan)"/>
    <path d="M0 730 C120 768 250 796 400 800 C500 802 560 780 600 766 L600 927 L0 927z" fill="var(--sky)"/>
    <path d="M0 742 C120 780 250 806 400 808 C500 809 560 786 600 772 L600 927 L0 927z" fill="var(--navy)"/>
    <path d="M600 732 C700 745 820 800 930 826 C1030 848 1120 800 1200 752 L1200 927 L600 927z" fill="var(--green-deep)"/>
    <path d="M600 742 C700 756 820 810 930 834 C1030 856 1120 812 1200 762 L1200 927 L600 927z" fill="var(--navy)"/>
  </svg>

  <h3 class="motto">Sleep Restfully. Live Fully.</h3>
  <p class="motto-note">Don't let poor sleep affect your heart health,<br>productivity, and long-term well-being.</p>

  <p class="contact-heading">Contact us today to schedule your Home Sleep Test!</p>
  <p class="contact-address">418 Willow Bend Rd,<br>Cedar Hollow, OK 74300</p>
  <p class="contact-phone" style="top:844px">+1 555-014-2873</p>
  <p class="contact-phone" style="top:880px">+1 555-017-6620</p>

  <div class="brand">
    <span class="brand-mark"></span>
    <span class="brand-name">Prairie Airway and Sleep Care</span>
  </div>

  <h1 class="cover-title">
    <span class="line-navy">Your Guide to a</span>
    <span class="line-green">Better Night’s Sleep</span>
  </h1>

  <p class="cover-lede">
    <strong>Home Sleep Study vs.<br>In-Lab Hospital Study:</strong>
    <span>Why Testing at Home is the Most Comfortable Choice for You.</span>
  </p>

  <div class="cover-footer">
    <p class="footer-name">Prairie Airway and Sleep Care</p>
    <p class="footer-tagline">Quality Care from the Comfort of Your Home</p>
  </div>

</main>
</body>
</html>
```